Postcard for Construction Industry

www.quarrymarkestimates.com is our website.

We offer services to construction companies to read blueprints and give them a materials quantity list of how much work they need to do on a project. We service all types of companies such as painting, flooring, siding, drywall, Acoustical ceiling tile, framing, millwork, and much more.

I want a postcard designed that can be sent via email AND regular mail to introduce our company.

I've also attached another document with more detailed explanation, pricing, etc.

Important:
The postcard must appeal to the construction industry so they pick it up and read it.

Target Market(s)

Construction Industry

Industry/Entity Type

Construction

Font styles to use
Serif

Requirements
Must have
• Call to Action -
• Register on our site
• Get a FREE Quote
• Trades Serviced should be referenced on front so the person reading it immediately knows 2 things. Free Construction Takeoffs. List of Trades.
Nice to have
• Construction Images
• It's so EASY!!!
• -You load your plans
• -We give you a quote
• -If you approve, we do the work!
• NO OBLIGATION TO PURCHASE
Should not have
• Pricing - other than FREE Quotes
• Should not have phone number Prominent. It can be small on the back. (I want them to register via website)

```html
<!DOCTYPE html>
<html lang="en">
<head>
<meta charset="utf-8">
<title>Quarrymark Estimates Postcard</title>
<link href="https://fonts.googleapis.com/css2?family=Oswald:wght@400;500&family=Montserrat:wght@500;600&family=Arimo:wght@400;700&display=swap" rel="stylesheet">
<style>
  :root {
    --navy: #1d3a5c;
    --blue: #1a8fd6;
    --blue-deep: #0f6fc0;
    --blue-light: #3aa8e8;
    --ink: #1c1c1c;
    --paper: #ffffff;
    --backdrop: #e9eaec;
    --rule: #b9bcc0;
  }
  * { box-sizing: border-box; margin: 0; padding: 0; }
  html, body { width: 915px; height: 1200px; overflow: hidden; }
  body { background: var(--backdrop); font-family: "Arimo", Arial, sans-serif; position: relative; }

  .card { position: absolute; width: 680px; height: 524px; background: var(--paper); overflow: hidden; box-shadow: 0 4px 14px rgba(0,0,0,.18); }
  .card--front { left: 85px; top: 51px; }
  .card--back { left: 144px; top: 626px; }

  .brand { position: absolute; }
  .brand__name { font-family: "Montserrat", sans-serif; font-weight: 600; color: var(--navy); letter-spacing: 1px; line-height: 1.05; }
  .brand__tag { font-family: "Montserrat", sans-serif; font-weight: 500; color: var(--blue); font-size: 8.5px; letter-spacing: .3px; margin-top: 4px; }

  .front-brand { left: 40px; top: 24px; }
  .front-brand .brand__name { font-size: 30px; }

  .service-line { position: absolute; left: 333px; top: 28px; color: var(--blue); font-size: 16px; }

  .trades-line { position: absolute; left: 26px; top: 120px; width: 260px; font-size: 11px; line-height: 1.4; color: var(--navy); }
  .trades-line strong { color: var(--blue); font-weight: 700; }

  .hero-photo { position: absolute; inset: 0; }

  .steps { position: absolute; left: 26px; top: 172px; }
  .steps__title { font-family: "Oswald", sans-serif; font-weight: 500; color: var(--blue); font-size: 32px; line-height: 1; margin-bottom: 10px; }
  .steps__list { list-style: none; font-size: 17px; color: var(--ink); line-height: 1.35; }
  .steps__note { font-family: "Oswald", sans-serif; color: var(--blue); font-size: 19px; margin-top: 14px; }

  .cta-band { position: absolute; left: 0; top: 0; width: 100%; height: 100%; }
  .cta { position: absolute; color: #fff; font-family: "Oswald", sans-serif; }
  .cta--quote { left: 18px; top: 378px; font-size: 20px; letter-spacing: .3px; }
  .cta--register { left: 55px; top: 422px; font-size: 15px; letter-spacing: .5px; }
  .site-pill { position: absolute; left: 16px; top: 454px; background: #f2f4f6; color: var(--navy); border-radius: 7px; padding: 4px 10px; font-family: "Oswald", sans-serif; font-size: 14px; letter-spacing: 1.3px; font-weight: 500; }

  .back-brand { left: 0; width: 403px; top: 34px; text-align: center; }
  .back-brand .brand__name { font-size: 30px; }

  .return-address { position: absolute; left: 412px; top: 22px; font-size: 8.5px; line-height: 1.45; color: var(--ink); font-style: normal; }
  .return-address__name { color: var(--blue); font-size: 13px; margin-bottom: 3px; }
  .stamp-box { position: absolute; left: 576px; top: 18px; width: 79px; height: 64px; border: 1.5px solid var(--rule); }
  .address-lines { position: absolute; left: 449px; top: 160px; width: 206px; }
  .address-lines span { display: block; height: 1.5px; background: var(--rule); margin-bottom: 26px; }

  .services { position: absolute; left: 0; top: 142px; width: 403px; height: 172px; background: linear-gradient(100deg, var(--blue-light), var(--blue-deep)); color: #fff; padding: 14px 20px 0; }
  .services__title { font-family: "Oswald", sans-serif; font-weight: 500; text-align: center; font-size: 15px; letter-spacing: .5px; line-height: 1.35; }
  .services__intro { font-size: 11.5px; margin-top: 12px; line-height: 1.25; }
  .services__trades { list-style: none; columns: 2; column-gap: 20px; font-size: 11.5px; margin-top: 8px; width: 300px; }
  .services__trades li { line-height: 1.7; display: flex; align-items: center; gap: 6px; }
  .services__trades svg { flex: none; }

  .blueprint-photo { position: absolute; left: 0; top: 318px; width: 403px; height: 141px; background: linear-gradient(160deg, #e8f0fa, #9cbde2 60%, #6b97cb); }
  .closing { position: absolute; left: 0; top: 459px; width: 403px; height: 65px; background: linear-gradient(100deg, var(--blue-light), var(--blue-deep)); color: #fff; text-align: center; font-weight: 700; font-size: 13.5px; line-height: 1.35; padding-top: 13px; }
</style>
</head>
<body>

<section class="card card--front">
  <svg class="hero-photo" width="680" height="524" viewBox="0 0 680 524" role="img" aria-label="Photo of smiling construction workers in hard hats reviewing a blueprint on a building site">
    <defs>
      <linearGradient id="heroTone" x1="0" y1="0" x2="1" y2="1">
        <stop offset="0" stop-color="#d9e4ee"/>
        <stop offset=".45" stop-color="#c9b08a"/>
        <stop offset="1" stop-color="#8fa3b8"/>
      </linearGradient>
    </defs>
    <polygon points="310,76 680,76 680,524 270,524" fill="url(#heroTone)"/>
  </svg>

  <div class="brand front-brand">
    <div class="brand__name">QUARRYMARK<br>ESTIMATES</div>
    <div class="brand__tag">COMMERCIAL CONSTRUCTION PROFESSIONALS</div>
  </div>

  <p class="service-line">Commercial Construction Takeoff Services</p>

  <p class="trades-line"><strong>FREE takeoffs for:</strong> Painting · Flooring · Siding · Drywall · Ceiling Tile · Framing · Millwork &amp; more</p>

  <div class="steps">
    <h2 class="steps__title">IT'S SO EASY!!!</h2>
    <ul class="steps__list">
      <li>You load your plans</li>
      <li>We give you a quote</li>
      <li>If you approve, we do the work!</li>
    </ul>
    <p class="steps__note">NO OBLIGATION TO PURCHASE!</p>
  </div>

  <svg class="cta-band" width="680" height="524" viewBox="0 0 680 524" aria-hidden="true">
    <defs>
      <linearGradient id="bandTone" x1="0" y1="0" x2="1" y2="0">
        <stop offset="0" stop-color="#1b86d2"/>
        <stop offset="1" stop-color="#3aa8e8"/>
      </linearGradient>
    </defs>
    <polygon points="0,348 316,348 292,508 0,508" fill="url(#bandTone)"/>
  </svg>

  <div class="cta cta--quote">GET A FREE QUOTE</div>
  <div class="cta cta--register">REGISTER ON OUR SITE</div>
  <div class="site-pill">WWW.QUARRYMARKESTIMATES.COM</div>
</section>

<section class="card card--back">
  <div class="brand back-brand">
    <div class="brand__name">QUARRYMARK<br>ESTIMATES</div>
    <div class="brand__tag">COMMERCIAL CONSTRUCTION PROFESSIONALS</div>
  </div>

  <address class="return-address">
    <div class="return-address__name">Quarrymark Estimates</div>
    PO Box 418<br>
    Millbrook, GA 30000<br>
    projects@quarrymarkestimates.com<br>
    555-014-2290
  </address>
  <div class="stamp-box"></div>
  <div class="address-lines"><span></span><span></span><span></span><span></span><span></span><span></span></div>

  <div class="services">
    <h2 class="services__title">AFFORDABLE, PROFESSIONAL, COMMERCIAL<br>BLUEPRINT QUANTITY TAKEOFFS</h2>
    <p class="services__intro">Our experts will assist you with commercial quantity takeoffs for most construction trades including:</p>
    <ul class="services__trades">
      <li><svg width="9" height="9" viewBox="0 0 10 10"><circle cx="5" cy="5" r="4.2" fill="none" stroke="#fff"/><path d="M4 3l2 2-2 2" fill="none" stroke="#fff"/></svg>Floor &amp; Wallcoverings</li>
      <li><svg width="9" height="9" viewBox="0 0 10 10"><circle cx="5" cy="5" r="4.2" fill="none" stroke="#fff"/><path d="M4 3l2 2-2 2" fill="none" stroke="#fff"/></svg>Painting</li>
      <li><svg width="9" height="9" viewBox="0 0 10 10"><circle cx="5" cy="5" r="4.2" fill="none" stroke="#fff"/><path d="M4 3l2 2-2 2" fill="none" stroke="#fff"/></svg>Sheetrock</li>
      <li><svg width="9" height="9" viewBox="0 0 10 10"><circle cx="5" cy="5" r="4.2" fill="none" stroke="#fff"/><path d="M4 3l2 2-2 2" fill="none" stroke="#fff"/></svg>Roofing</li>
      <li><svg width="9" height="9" viewBox="0 0 10 10"><circle cx="5" cy="5" r="4.2" fill="none" stroke="#fff"/><path d="M4 3l2 2-2 2" fill="none" stroke="#fff"/></svg>Siding</li>
      <li><svg width="9" height="9" viewBox="0 0 10 10"><circle cx="5" cy="5" r="4.2" fill="none" stroke="#fff"/><path d="M4 3l2 2-2 2" fill="none" stroke="#fff"/></svg>Foundations &amp; Paving</li>
    </ul>
  </div>

  <div class="blueprint-photo" role="img" aria-label="Photo of rolled blueprints resting on an open construction plan"></div>

  <p class="closing">Get a FREE CUSTOM QUOTE on every project takeoff!<br>No obligation to purchase!</p>
</section>

</body>
</html>
```